High-End Bifold Brochure for Aesthetics Medspa Business

I need a print-ready, bifold brochure designed for a high-end, luxurious Aesthetics/Medspa practice.

The brochure will showcase the latest IV Therapy content (6 options included in MENU.docx), and exclusive Vitamin B12+ wellness shot content (included in LS PDF). It should also include the business logo and basic office contact options.

The design should be clean, modern, and appealing with a light design. It should flow nicely and compliment the website theme/design. Preferably, having the 6 IV treatments inside bifold, with B12 shot on back/outside page. For easy viewing.

I have attached a few licensed images, if you think they will incorporate into the design nicely. Otherwise, please ignore them. If needed, I can send more.

https://lunavelleskincareclinic.com/
Brand purple: #491c64
Fonts used on site:
Josefin Sans
Montserrat

Size should be 6.5 x 9 using specs on Quillapress's template page (Half Fold design)
https://www.quillapress.com/resources/templates

• Montserrat, Josefin Sans, or similar

• Content included in MENU + B12 shot content on PDF.
Similar feel to the website, High-end, modern, luxurious

```html
<!DOCTYPE html>
<html lang="en">
<head>
<meta charset="utf-8">
<title>Lunavelle Skincare – Bifold Brochure</title>
<link href="https://fonts.googleapis.com/css2?family=Josefin+Sans:wght@400;600;700&family=Montserrat:wght@400;500;600&display=swap" rel="stylesheet">
<style>
  :root{
    --purple:#491c64;
    --purple-soft:#7a4a98;
    --ink:#2b2230;
    --grey:#6c6670;
    --paper:#ffffff;
    --canvas:#ececec;
    --on-purple:#e8def0;
    --photo-a:#e9d9cf;
    --photo-b:#c8a994;
    --team-a:#b9b4bd;
    --team-b:#5f5566;
  }
  *{box-sizing:border-box;margin:0;padding:0}
  html,body{width:1200px;height:3000px;overflow:hidden}
  body{background:var(--canvas);font-family:"Montserrat",sans-serif;color:var(--ink);position:relative}
  .spread{position:absolute;left:50px;width:1100px;height:793px;display:flex;box-shadow:0 4px 14px rgba(0,0,0,.18)}
  .spread--outside{top:657px}
  .spread--inside{top:1550px}
  .page{position:relative;width:550px;height:793px;overflow:hidden;background:var(--paper)}
  .page svg.art{position:absolute;left:0;top:0}
  .abs{position:absolute}

  /* back page */
  .back{background:var(--purple);color:#fff}
  .back .title{left:40px;top:284px;font-family:"Josefin Sans",sans-serif;font-size:17px;line-height:23px;font-weight:400}
  .back .title b{font-weight:700}
  .nutrient{position:absolute;width:230px;padding-left:22px}
  .nutrient .tick{position:absolute;left:0;top:0}
  .nutrient h4{font-family:"Josefin Sans",sans-serif;font-size:13px;font-weight:600;margin-bottom:5px}
  .nutrient p{font-size:7.6px;line-height:10.5px;color:var(--on-purple)}
  .brand{display:flex;align-items:center;gap:8px;font-family:"Josefin Sans",sans-serif;font-weight:600;font-size:13px;line-height:15px;text-transform:uppercase;letter-spacing:.5px}
  .brand .mark{width:30px;height:30px;border-radius:50%;border:1.5px solid currentColor;flex:none}
  .back .brand{left:40px;top:712px;color:#fff}
  .connect{left:274px;top:680px;width:250px}
  .connect h4{font-family:"Josefin Sans",sans-serif;font-size:13px;font-weight:600;margin-bottom:10px}
  .connect .row{display:flex;gap:14px}
  .connect .item{display:flex;gap:6px;font-size:7.4px;line-height:10px;margin-bottom:8px;align-items:flex-start}
  .connect .dots{display:flex;gap:6px;margin-top:2px}
  .connect .dots span{width:8px;height:8px;border-radius:50%;background:#fff}

  /* cover */
  .cover .brand{left:40px;top:36px;color:var(--purple)}
  .cover .city{left:40px;top:540px;font-family:"Josefin Sans",sans-serif;font-size:36px;font-weight:600;letter-spacing:1px;color:var(--ink)}
  .cover .headline{left:40px;top:580px;font-family:"Josefin Sans",sans-serif;font-size:38px;font-weight:700;letter-spacing:1px;color:var(--purple)}
  .cover .rule{left:40px;top:628px;width:340px;height:4px;background:var(--purple)}
  .cover .call{left:40px;top:652px;font-family:"Josefin Sans",sans-serif;font-size:18px;line-height:21px;color:var(--ink)}
  .cover .call b{color:var(--purple);font-weight:600}
  .cover .phone{left:40px;top:698px;font-family:"Josefin Sans",sans-serif;font-size:24px;font-weight:600;letter-spacing:.5px}
  .cover .web{left:40px;top:746px;font-size:8.5px;color:var(--ink)}
  .cover .webline{left:200px;top:752px;width:315px;height:1px;background:#c9c4cc}

  /* page 2 */
  .portrait{left:40px;top:40px;width:105px;height:105px;border-radius:50%;background:radial-gradient(circle at 50% 40%,var(--photo-a),var(--photo-b));border:3px solid #fff;box-shadow:0 0 0 1px #ddd}
  .doc-name{left:165px;top:44px;font-family:"Josefin Sans",sans-serif;font-size:17px;font-weight:700;color:var(--purple)}
  .doc-cred{left:165px;top:68px;font-family:"Josefin Sans",sans-serif;font-size:16px;color:var(--ink)}
  .bio{font-size:8.2px;line-height:12px;color:var(--grey);text-align:justify}
  .bio--lead{left:165px;top:98px;width:345px}
  .bio--a{left:40px;top:222px;width:470px}
  .bio--b{left:40px;top:290px;width:470px}
  .section-title{font-family:"Josefin Sans",sans-serif;font-size:14px;font-weight:700;color:var(--purple);letter-spacing:.5px}
  .benefits-title{left:40px;top:378px}
  .benefits-rule{left:40px;top:396px;width:138px;height:1px;background:var(--purple)}
  .benefits{left:40px;top:414px;width:250px;list-style:none}
  .benefits li{position:relative;padding-left:26px;font-size:8.4px;line-height:11.5px;color:var(--ink);margin-bottom:14px}
  .benefits li svg{position:absolute;left:0;top:0}
  .staff-photo{left:314px;top:396px;width:196px;height:300px;border-radius:14px;background:linear-gradient(160deg,#f3efee,var(--photo-a) 50%,#3a3140);box-shadow:0 2px 6px rgba(0,0,0,.2)}
  .folio{bottom:0;width:30px;height:56px;background:var(--purple);color:#fff;font-family:"Josefin Sans",sans-serif;font-weight:700;font-size:13px;display:flex;align-items:center;justify-content:center}
  .folio--left{left:39px}
  .folio--right{right:39px}
  .footer-web{bottom:28px;font-size:7.6px;color:var(--purple-soft)}

  /* page 3 */
  .haven-title{left:40px;top:142px}
  .haven-sub{left:40px;top:170px;font-family:"Josefin Sans",sans-serif;font-size:13px;font-weight:600;color:var(--purple);letter-spacing:.5px}
  .infusion{position:absolute;left:42px;width:470px;padding-left:52px}
  .infusion .icon{position:absolute;left:0;top:0;width:34px;height:34px;border-radius:50%;background:var(--purple);display:flex;align-items:center;justify-content:center}
  .infusion h4{font-size:8.6px;font-weight:600;text-transform:uppercase;color:var(--ink);margin:3px 0 6px}
  .infusion h4 span{text-transform:none;font-weight:500}
  .infusion p{font-size:8px;line-height:11px;color:var(--grey)}
</style>
</head>
<body>

<section class="spread spread--outside">

  <article class="page back">
    <svg class="art" width="550" height="260" viewBox="0 0 550 260">
      <defs>
        <linearGradient id="injectGrad" x1="0" y1="0" x2="1" y2="1">
          <stop offset="0" stop-color="#f4ecea"/>
          <stop offset="1" stop-color="#d6b9a6"/>
        </linearGradient>
      </defs>
      <path d="M0 0 H440 Q360 200 0 214 Z" fill="#fff"/>
      <path d="M0 214 Q360 200 440 0 H452 Q380 214 0 228 Z" fill="var(--purple-soft)" opacity=".7"/>
      <path role="img" aria-label="Photo of a woman receiving a facial injection from a gloved practitioner" d="M0 0 H420 Q340 178 0 196 Z" fill="url(#injectGrad)"/>
    </svg>

    <h2 class="abs title"><b>Dr. Velloro's</b> Vitamin B12 Cocktail's<br>Essential Vitamins And Nutrients</h2>

    <div class="nutrient" style="left:40px;top:343px">
      <svg class="tick" width="14" height="14" viewBox="0 0 14 14"><circle cx="7" cy="7" r="6" fill="none" stroke="#fff" stroke-width="1.4"/><path d="M4 7.2l2 2 4-4.3" fill="none" stroke="#fff" stroke-width="1.4"/></svg>
      <h4>Thiamine</h4><p>Is used by the body to metabolize food for energy and maintain proper health and nerve function.</p>
    </div>
    <div class="nutrient" style="left:40px;top:393px">
      <svg class="tick" width="14" height="14" viewBox="0 0 14 14"><circle cx="7" cy="7" r="6" fill="none" stroke="#fff" stroke-width="1.4"/><path d="M4 7.2l2 2 4-4.3" fill="none" stroke="#fff" stroke-width="1.4"/></svg>
      <h4>Niacinamide</h4><p>Helps maintain a healthy cardiovascular system and metabolism, brain function, healthy skin formation, and aids in the prevention of diabetes.</p>
    </div>
    <div class="nutrient" style="left:40px;top:462px">
      <svg class="tick" width="14" height="14" viewBox="0 0 14 14"><circle cx="7" cy="7" r="6" fill="none" stroke="#fff" stroke-width="1.4"/><path d="M4 7.2l2 2 4-4.3" fill="none" stroke="#fff" stroke-width="1.4"/></svg>
      <h4>Hydroxocobalamin</h4><p>Helps with DNA synthesis and supports replication, it also helps in the body's use of fats and carbohydrates for energy, and in making new proteins.</p>
    </div>
    <div class="nutrient" style="left:40px;top:528px">
      <svg class="tick" width="14" height="14" viewBox="0 0 14 14"><circle cx="7" cy="7" r="6" fill="none" stroke="#fff" stroke-width="1.4"/><path d="M4 7.2l2 2 4-4.3" fill="none" stroke="#fff" stroke-width="1.4"/></svg>
      <h4>Inositol</h4><p>Aids in the metabolic breakdown of fats, and helps reduce blood cholesterol.</p>
    </div>
    <div class="nutrient" style="left:40px;top:580px">
      <svg class="tick" width="14" height="14" viewBox="0 0 14 14"><circle cx="7" cy="7" r="6" fill="none" stroke="#fff" stroke-width="1.4"/><path d="M4 7.2l2 2 4-4.3" fill="none" stroke="#fff" stroke-width="1.4"/></svg>
      <h4>Chromium</h4><p>Helps move sugars from the blood system, and turn fats, carbs, and proteins into energy.</p>
    </div>

    <div class="nutrient" style="left:274px;top:343px">
      <svg class="tick" width="14" height="14" viewBox="0 0 14 14"><circle cx="7" cy="7" r="6" fill="none" stroke="#fff" stroke-width="1.4"/><path d="M4 7.2l2 2 4-4.3" fill="none" stroke="#fff" stroke-width="1.4"/></svg>
      <h4>Riboflavin</h4><p>Acts as an antioxidant within the body. Riboflavin prevents free radical damage and protects skin and eye health.</p>
    </div>
    <div class="nutrient" style="left:274px;top:393px">
      <svg class="tick" width="14" height="14" viewBox="0 0 14 14"><circle cx="7" cy="7" r="6" fill="none" stroke="#fff" stroke-width="1.4"/><path d="M4 7.2l2 2 4-4.3" fill="none" stroke="#fff" stroke-width="1.4"/></svg>
      <h4>Pyridoxine</h4><p>Is important for brain development and keeping the nervous and immune systems healthy.</p>
    </div>
    <div class="nutrient" style="left:274px;top:462px">
      <svg class="tick" width="14" height="14" viewBox="0 0 14 14"><circle cx="7" cy="7" r="6" fill="none" stroke="#fff" stroke-width="1.4"/><path d="M4 7.2l2 2 4-4.3" fill="none" stroke="#fff" stroke-width="1.4"/></svg>
      <h4>Molybdenum</h4><p>Aids in tissue growth and repair, as well as promoting healthy hair, skin, and nails.</p>
    </div>
    <div class="nutrient" style="left:274px;top:528px">
      <svg class="tick" width="14" height="14" viewBox="0 0 14 14"><circle cx="7" cy="7" r="6" fill="none" stroke="#fff" stroke-width="1.4"/><path d="M4 7.2l2 2 4-4.3" fill="none" stroke="#fff" stroke-width="1.4"/></svg>
      <h4>L-carnitine</h4><p>Helps convert fatty acids into energy.</p>
    </div>

    <div class="abs brand"><span class="mark"></span><span>Lunavelle Skincare<br>&amp; Aesthetics</span></div>

    <div class="abs connect">
      <h4>Connect With Us</h4>
      <div class="row">
        <div>
          <div class="item">
            <svg width="9" height="11" viewBox="0 0 9 11"><path d="M4.5 0.5a4 4 0 0 1 4 4c0 3-4 6-4 6s-4-3-4-6a4 4 0 0 1 4-4z" fill="#fff"/><circle cx="4.5" cy="4.5" r="1.4" fill="var(--purple)"/></svg>
            <span>2140 E Marigold Way,<br>Unit 101 Tucson, Arizona 85718</span>
          </div>
          <div class="item">
            <svg width="10" height="8" viewBox="0 0 10 8"><rect x=".5" y=".5" width="9" height="7" fill="#fff"/><path d="M.5 .8L5 4.5 9.5 .8" fill="none" stroke="var(--purple)" stroke-width="1"/></svg>
            <span>info@lunavelleskincareclinic.com</span>
          </div>
          <div class="dots"><span></span><span></span><span></span><span></span></div>
        </div>
        <div>
          <div class="item">
            <svg width="10" height="10" viewBox="0 0 10 10"><circle cx="5" cy="5" r="4.3" fill="none" stroke="#fff" stroke-width="1"/><path d="M.7 5h8.6M5 .7c2 2.5 2 6.1 0 8.6M5 .7c-2 2.5-2 6.1 0 8.6" fill="none" stroke="#fff" stroke-width=".8"/></svg>
            <span>lunavelleskincare<br>clinic.com</span>
          </div>
          <div class="item">
            <svg width="10" height="10" viewBox="0 0 10 10"><path d="M2 .5l2 2.2-1 1.4a6 6 0 0 0 3 3l1.4-1 2.1 2-1.3 1.4C4.5 9.3.8 5.6.6 2z" fill="#fff"/></svg>
            <span>(555) 790-1234</span>
          </div>
        </div>
      </div>
    </div>
  </article>

  <article class="page cover">
    <svg class="art" width="550" height="540" viewBox="0 0 550 540">
      <defs>
        <linearGradient id="faceGrad" x1="0" y1="0" x2="1" y2="1">
          <stop offset="0" stop-color="#f2e4da"/>
          <stop offset=".6" stop-color="var(--photo-b)"/>
          <stop offset="1" stop-color="#8a6a57"/>
        </linearGradient>
        <linearGradient id="teamGrad" x1="0" y1="0" x2="1" y2="1">
          <stop offset="0" stop-color="var(--team-a)"/>
          <stop offset="1" stop-color="var(--team-b)"/>
        </linearGradient>
      </defs>
      <path role="img" aria-label="Portrait photo of a woman with smooth glowing skin" d="M210 128 Q380 52 550 24 V340 Q380 262 210 128 Z" fill="url(#faceGrad)"/>
      <path role="img" aria-label="Photo of the clinic's doctor and staff team in front of a glittering wall" d="M0 158 Q110 126 210 128 Q380 262 550 340 Q330 450 0 488 Z" fill="url(#teamGrad)"/>
      <path d="M210 128 Q380 262 550 340" fill="none" stroke="#fff" stroke-width="3"/>
      <path d="M130 120 Q330 20 550 0 V24 Q380 52 210 128 Q170 120 130 120 Z" fill="var(--purple)"/>
      <path d="M0 488 Q330 450 550 340 V392 Q340 500 0 520 Z" fill="var(--purple)"/>
    </svg>

    <div class="abs brand"><span class="mark"></span><span>Lunavelle Skincare<br>&amp; Aesthetics</span></div>

    <h1 class="abs city">TUCSON'S</h1>
    <p class="abs headline">PREMIER MEDSPA</p>
    <div class="abs rule"></div>
    <p class="abs call"><b>CALL TODAY</b><br>FOR YOUR FREE CONSULTATION</p>
    <p class="abs phone">(555) 790-1234</p>
    <p class="abs web">www.lunavelleskincareclinic.com</p>
    <div class="abs webline"></div>
  </article>
</section>

<section class="spread spread--inside">

  <article class="page">
    <div class="abs portrait" role="img" aria-label="Portrait photo of Dr. Adrian Velloro"></div>
    <h2 class="abs doc-name">Dr. Adrian Velloro</h2>
    <p class="abs doc-cred">M.D., F.A.C.S.</p>

    <p class="abs bio bio--lead">As Founder and Medical Director of Lunavelle Skincare &amp; Aesthetics, Dr. Adrian Velloro, M.D., F.A.C.S. has over 38 years of experience. Dr. Velloro's thorough knowledge of anatomy, artistic talent, and attention to detail enable his skillful and precise use of neuromodulators and fillers to minimize lines, wrinkles and volume loss of the face. Dr. Velloro customizes all treatments according to his patient's individual needs and personally administers all treatments. His patients consistently experience exemplary results with the restoration of a natural and youthful appearance.</p>
    <p class="abs bio bio--a">Dr. Velloro has been recognized by the Society of Aesthetic Care Practitioners as a Top Physician in Facial Rejuvenation and Aesthetics and spotlighted in the Annual Register of Noted Clinicians. He is a fellow of the Collegium of Reconstructive Surgeons. He is on the faculty of Desert Ridge Medical School, and is a certified Medical Laser Technician and Laser Safety Officer. He was listed in the Honor Roll of Practitioners in the State of Arizona.</p>
    <p class="abs bio bio--b">Dr. Velloro is wholeheartedly committed to offering the highest quality care in a safe and compassionate environment. He continuously seeks and implements state of the art technology in his practice, and he and his highly trained staff regularly complete rigorous continuing education in the most current approaches to patient care and customer service.</p>

    <h3 class="abs section-title benefits-title">OVERALL BENEFITS</h3>
    <div class="abs benefits-rule"></div>
    <ul class="abs benefits">
      <li><svg width="14" height="14" viewBox="0 0 14 14"><circle cx="7" cy="7" r="7" fill="var(--purple)"/><path d="M4 7.2l2 2 4-4.3" fill="none" stroke="#fff" stroke-width="1.4"/></svg>B12 helps aid in red blood cell formation and in DNA synthesis</li>
      <li><svg width="14" height="14" viewBox="0 0 14 14"><circle cx="7" cy="7" r="7" fill="var(--purple)"/><path d="M4 7.2l2 2 4-4.3" fill="none" stroke="#fff" stroke-width="1.4"/></svg>Aids in the healthy maintenance of the immune and nervous systems, and the optic nerve</li>
      <li><svg width="14" height="14" viewBox="0 0 14 14"><circle cx="7" cy="7" r="7" fill="var(--purple)"/><path d="M4 7.2l2 2 4-4.3" fill="none" stroke="#fff" stroke-width="1.4"/></svg>Helps improve skin tone, and strengthen nails and hair</li>
      <li><svg width="14" height="14" viewBox="0 0 14 14"><circle cx="7" cy="7" r="7" fill="var(--purple)"/><path d="M4 7.2l2 2 4-4.3" fill="none" stroke="#fff" stroke-width="1.4"/></svg>Boosts metabolism and energy (which may help reduce craving and encourage weight loss)</li>
      <li><svg width="14" height="14" viewBox="0 0 14 14"><circle cx="7" cy="7" r="7" fill="var(--purple)"/><path d="M4 7.2l2 2 4-4.3" fill="none" stroke="#fff" stroke-width="1.4"/></svg>Helps relieve cramping and bloating</li>
      <li><svg width="14" height="14" viewBox="0 0 14 14"><circle cx="7" cy="7" r="7" fill="var(--purple)"/><path d="M4 7.2l2 2 4-4.3" fill="none" stroke="#fff" stroke-width="1.4"/></svg>Improves memory (which may protect against memory loss)</li>
      <li><svg width="14" height="14" viewBox="0 0 14 14"><circle cx="7" cy="7" r="7" fill="var(--purple)"/><path d="M4 7.2l2 2 4-4.3" fill="none" stroke="#fff" stroke-width="1.4"/></svg>Enhances mood and lessens the effects of depression</li>
    </ul>

    <div class="abs staff-photo" role="img" aria-label="Photo of a smiling staff member in a black uniform and gloves"></div>

    <div class="abs folio folio--left">2</div>
    <p class="abs footer-web" style="left:363px">www.lunavelleskincareclinic.com</p>
  </article>

  <article class="page">
    <svg class="art" width="550" height="150" viewBox="0 0 550 150">
      <defs>
        <linearGradient id="lipsGrad" x1="0" y1="0" x2="1" y2="0">
          <stop offset="0" stop-color="#f3e3da"/>
          <stop offset=".5" stop-color="#d9a99a"/>
          <stop offset="1" stop-color="#efe6e2"/>
        </linearGradient>
      </defs>
      <path role="img" aria-label="Close-up photo of lips receiving a filler injection" d="M0 0 H550 V100 Q420 90 300 112 Q120 80 0 40 Z" fill="url(#lipsGrad)"/>
      <path d="M200 118 Q400 80 550 100 V125 Q400 108 200 118 Z" fill="var(--purple)"/>
    </svg>

    <h2 class="abs section-title haven-title">THE INFUSION HAVEN</h2>
    <p class="abs haven-sub">IV THERAPY</p>

    <div class="infusion" style="top:212px">
      <div class="icon"><svg width="14" height="16" viewBox="0 0 14 16"><path d="M7 1C7 1 2 7 2 10a5 5 0 0 0 10 0C12 7 7 1 7 1z" fill="none" stroke="#fff" stroke-width="1.3"/></svg></div>
      <h4>Immunity Booster $150</h4>
      <p>Have a cold, flu or just need to give your immunity a boost?<br>Let us mix a powerful punch in our booster bag just for you to prevent or relieve aches and pain.</p>
    </div>
    <div class="infusion" style="top:300px">
      <div class="icon"><svg width="14" height="16" viewBox="0 0 14 16"><path d="M7 1C7 1 2 7 2 10a5 5 0 0 0 10 0C12 7 7 1 7 1z" fill="none" stroke="#fff" stroke-width="1.3"/></svg></div>
      <h4>Refresh &amp; Hydrate $100</h4>
      <p>Relieve dehydration from the extremes of lifestyle with our balanced electrolyte cocktail targeting jet lag, fatigue, stress and sports related activity to leave you feeling more youthful and refreshed!</p>
    </div>
    <div class="infusion" style="top:378px">
      <div class="icon"><svg width="14" height="16" viewBox="0 0 14 16"><path d="M7 1C7 1 2 7 2 10a5 5 0 0 0 10 0C12 7 7 1 7 1z" fill="none" stroke="#fff" stroke-width="1.3"/></svg></div>
      <h4>Migraine Buster $150</h4>
      <p>Eradicate your migraine pain, nausea, vomiting, and light sensitivity with our magic formula.</p>
    </div>
    <div class="infusion" style="top:446px">
      <div class="icon"><svg width="14" height="16" viewBox="0 0 14 16"><path d="M7 1C7 1 2 7 2 10a5 5 0 0 0 10 0C12 7 7 1 7 1z" fill="none" stroke="#fff" stroke-width="1.3"/></svg></div>
      <h4>Wellness Infusion: <span>Velloro Cocktail</span> $180</h4>
      <p>This infusion of vitamins, minerals and electrolytes results in direct access of these nutrients into your cells, enhancing energy, decreasing stress and anxiety in addition to improving memory. Other benefits include relief of asthma, depression, allergies and fibromyalgia pain.</p>
    </div>
    <div class="infusion" style="top:532px">
      <div class="icon"><svg width="14" height="16" viewBox="0 0 14 16"><path d="M7 1C7 1 2 7 2 10a5 5 0 0 0 10 0C12 7 7 1 7 1z" fill="none" stroke="#fff" stroke-width="1.3"/></svg></div>
      <h4>Glo $200</h4>
      <p>A beauty mixture of Glutathione, Biotin and our special formula created to strengthen your hair, nails and skin for that SPECIAL LOOK!</p>
    </div>
    <div class="infusion" style="top:602px">
      <div class="icon"><svg width="14" height="16" viewBox="0 0 14 16"><path d="M7 1C7 1 2 7 2 10a5 5 0 0 0 10 0C12 7 7 1 7 1z" fill="none" stroke="#fff" stroke-width="1.3"/></svg></div>
      <h4>The Ultimate Weight Loss Infusion $200</h4>
      <p>Our unique fat burning formula targets fatty deposits resulting in fat expulsion from the body resulting in a more defined and contoured appearance.</p>
    </div>
    <div class="infusion" style="top:668px">
      <div class="icon"><svg width="14" height="16" viewBox="0 0 14 16"><path d="M7 1C7 1 2 7 2 10a5 5 0 0 0 10 0C12 7 7 1 7 1z" fill="none" stroke="#fff" stroke-width="1.3"/></svg></div>
      <h4>NAD+ IV: The Fountain of Youth (+) $350</h4>
      <p>Anti-aging co-enzyme NAD+ in conjunction with Vitamins elevates brain health and beauty, all in one IV treatment!</p>
    </div>

    <p class="abs footer-web" style="left:40px">www.lunavelleskincareclinic.com</p>
    <div class="abs folio folio--right">3</div>
  </article>
</section>

</body>
</html>
```